Hollowmere Dental Center Specials/Offers

Take the advertisement pic (LABELED ADVERTISEMENT) and make it look "professional in appearance" using the logo and color scheme of Hollowmere Dental Center. The Phone number should be 719-555-0186. I want the same content, different background, professional looking document. I want it to be a 12"x12" document. High resolution files should include .PDF, .JPG and .AI. Any or all documents can be used for colors and overall scheme. I would like to have the overall colors include the main blue color from the file 4db749b4ef4c5e0717512bf7eb26bf54 and include the brown "swoosh" somewhere through/on the final document. Stock files of smiling young families can be used but not required. I am on a tight time-line and have placed 5 days as the deadline, but I will pick my favorite in as little as 2-3 days if I can get a good product. Again ALL the info from the Advertisement document should be included on the final product. Use any or all of the uploaded files for assistance. You can also visit our website for more info: www.hollowmeredentalcenter.example Thanks

```html
<!DOCTYPE html>
<html lang="en">
<head>
<meta charset="utf-8">
<title>Hollowmere Dental Center – Specials &amp; Offers</title>
<link rel="stylesheet" href="https://fonts.googleapis.com/css2?family=Montserrat:wght@600;700&family=Didact+Gothic&display=swap">
<style>
  :root {
    --teal-deep: #1d4656;
    --teal-mid: #4e7686;
    --teal-soft: #8eaab4;
    --teal-pale: #b9ccd3;
    --leaf-text: #284a59;
    --brown: #5b4440;
    --brown-dark: #463431;
    --white: #ffffff;
    --logo-brown: #5d4a45;
    --font-bold: "Montserrat", Arial, sans-serif;
    --font-light: "Didact Gothic", "Century Gothic", sans-serif;
  }
  * { margin: 0; padding: 0; box-sizing: border-box; }
  html, body { width: 1200px; height: 1200px; overflow: hidden; background: var(--teal-deep); }
  .ad { position: relative; width: 1200px; height: 1200px; overflow: hidden; color: var(--white); }
  .ad-art { position: absolute; inset: 0; }
  .brand { position: absolute; left: 118px; top: 82px; display: flex; align-items: center; gap: 18px; }
  .brand-dot { width: 26px; height: 26px; border-radius: 50%; background: var(--teal-soft); }
  .brand-name { font-family: var(--font-light); font-size: 38px; color: var(--logo-brown); line-height: 1.15; }
  .headline {
    position: absolute; left: 590px; top: 54px; width: 596px; text-align: center;
    font-family: var(--font-bold); font-weight: 700; font-size: 43px; line-height: 1.33;
    text-transform: uppercase; white-space: nowrap; letter-spacing: -0.5px;
  }
  .offer-main { position: absolute; left: 98px; top: 340px; }
  .offer-main .big { font-family: var(--font-light); font-size: 64px; line-height: 1; }
  .note { font-family: var(--font-bold); font-weight: 600; font-size: 18px; margin-top: 24px; }
  .bullet { position: absolute; left: 98px; }
  .bullet::before {
    content: ""; position: absolute; left: -58px; top: 10px; width: 32px; height: 32px;
    border-radius: 50%; background: var(--teal-pale);
  }
  .bullet h2 { font-family: var(--font-bold); font-weight: 700; font-size: 33px; line-height: 1.18; }
  .bullet p.list { font-family: var(--font-light); font-size: 28px; line-height: 1.4; margin-top: 4px; }
  .bullet .note { margin-top: 12px; }
  .bullet-providers { top: 522px; }
  .bullet-exam { top: 744px; }
  .cta {
    position: absolute; left: 0; top: 975px; width: 652px; height: 150px;
    background: linear-gradient(90deg, var(--brown-dark), var(--brown));
    border-radius: 0 6px 6px 0; padding: 16px 0 0 104px;
  }
  .cta-label { font-family: var(--font-bold); font-weight: 700; font-size: 31px; }
  .cta-phone { font-family: var(--font-light); font-size: 68px; letter-spacing: 7px; line-height: 1.2; }
  .website { position: absolute; left: 108px; top: 1136px; font-family: var(--font-light); font-size: 32px; letter-spacing: 0.5px; }
  .leaf-label { position: absolute; font-family: var(--font-bold); font-weight: 700; color: var(--leaf-text); text-align: center; line-height: 1.15; }
  .leaf-bleach { left: 645px; top: 818px; font-size: 25px; transform: rotate(-13deg); }
  .leaf-referral { left: 930px; top: 975px; font-size: 25px; transform: rotate(-62deg); }
</style>
</head>
<body>
<main class="ad">
  <svg class="ad-art" width="1200" height="1200" viewBox="0 0 1200 1200">
    <defs>
      <linearGradient id="bg" x1="0" y1="0" x2="1" y2="0.3">
        <stop offset="0" stop-color="#1f4a5a"/>
        <stop offset="0.55" stop-color="#5d8392"/>
        <stop offset="1" stop-color="#2c5566"/>
      </linearGradient>
      <linearGradient id="leaf" x1="0" y1="0" x2="1" y2="1">
        <stop offset="0" stop-color="#9db6bf"/>
        <stop offset="1" stop-color="#5f8594"/>
      </linearGradient>
      <linearGradient id="leaf-light" x1="0" y1="0" x2="1" y2="1">
        <stop offset="0" stop-color="#b3c8cf"/>
        <stop offset="1" stop-color="#86a4b0"/>
      </linearGradient>
      <linearGradient id="photo" x1="0" y1="0" x2="1" y2="1">
        <stop offset="0" stop-color="#e8e3de"/>
        <stop offset="0.5" stop-color="#c9a58e"/>
        <stop offset="1" stop-color="#6e5a54"/>
      </linearGradient>
      <path id="arc-text" d="M408,390 C620,300 930,330 1115,500"/>
    </defs>
    <rect class="bg" width="1200" height="1200" fill="url(#bg)"/>
    <path class="header-panel" d="M0,0 H690 C560,110 470,290 320,300 C200,305 90,270 0,255 Z" fill="#f7f7f7"/>
    <path class="header-edge" d="M690,0 C600,90 520,200 455,225 C530,190 620,90 700,0 Z" fill="#d5e0e4"/>
    <path class="leaf-frame" d="M530,330 C720,250 1000,300 1165,520 C1060,700 880,760 700,720 C880,700 1040,640 1130,520 C980,350 720,300 530,330 Z" fill="url(#leaf)" opacity="0.8"/>
    <path class="photo-window" role="img" aria-label="Stock photo of a smiling young family: father, son and mother" d="M470,400 C650,350 960,360 1150,520 C1050,660 900,710 720,695 C600,680 530,520 470,400 Z" fill="url(#photo)"/>
    <path class="brown-swoosh" d="M1160,282 C1185,310 1195,340 1200,360 L1200,330 C1190,310 1175,292 1160,282 Z" fill="#6a4d45"/>
    <path class="leaf-bleach-shape" d="M560,910 C640,785 800,725 955,742 C925,860 780,950 600,975 C585,955 570,932 560,910 Z" fill="url(#leaf-light)"/>
    <path class="brown-swoosh" d="M940,745 C1050,760 1150,820 1200,880 L1200,905 C1140,835 1050,775 940,745 Z" fill="#6a4d45"/>
    <path class="leaf-referral-shape" d="M880,1200 C870,1060 960,930 1110,880 C1160,970 1150,1120 1060,1200 Z" fill="url(#leaf-light)"/>
    <path class="leaf-vein" d="M900,1190 C960,1060 1040,960 1110,890" stroke="#cbd9de" stroke-width="3" fill="none"/>
    <text font-family="Didact Gothic, sans-serif" font-size="38" fill="#ffffff" letter-spacing="1.5"><textPath href="#arc-text">Treatment scheduled on your first visit.</textPath></text>
  </svg>

  <div class="brand"><span class="brand-dot"></span><span class="brand-name">Hollowmere<br>Dental Center</span></div>

  <h1 class="headline">Where<br>the whole family<br>can be seen!</h1>

  <section class="offer-main">
    <p class="big">20% OFF</p>
    <p class="note">Only patiens without Dental Benefits</p>
  </section>

  <section class="bullet bullet-providers">
    <h2>Preferred Provider For:</h2>
    <p class="list">Summit Dental, Lifeway, Cedarline,<br>Alderpoint Health and Unity Harmonia</p>
    <p class="note">We take all other non-HMO plans</p>
  </section>

  <section class="bullet bullet-exam">
    <h2>$59 New patiens X-Rays<br>Comprehensive exam<br>Regular Cleaning</h2>
    <p class="note">Only patiens without Dental Benefits</p>
  </section>

  <p class="leaf-label leaf-bleach">$99<br>Bleaching Special</p>
  <p class="leaf-label leaf-referral">Ask about<br>Referral<br>Program</p>

  <section class="cta">
    <p class="cta-label">Call Today for an Appointment</p>
    <p class="cta-phone">719-555-0186</p>
  </section>

  <p class="website">www.hollowmeredentalcenter.example</p>
</main>
</body>
</html>
```